Business Card, A4 Letter Head and DL Envelope for Vantrelle

We are looking for a design for our Business Card, A4 Letter Head and DL Envelope.

Vantrelle is a distributor of promotional products. We specialize in a range of branded promotional products, these include pens, polo shirts, key rings, drink bottles, uniforms and bags to name a few. We are experts in marketing and assist companies in choosing the right promotional product for their needs. We will predominately be an online business where customers visit our website and browse our range of promotional products and branding options.

Our colours are black, red, white and grey.

Files must be supplied in eps, pdf and ai format.

Please display the following information:
Corbin Hale
Account Manager
Suite xxx, 214 Dawlish Parade Melbourne, Victoria 3000
Phone +61 3 5550 1827
Mobile +61 455 501 936
sales@vantrelle.com.au
www.vantrelle.com.au

```html
<!DOCTYPE html>
<html lang="en">
<head>
<meta charset="utf-8">
<title>Vantrelle Stationery</title>
<link rel="stylesheet" href="https://fonts.googleapis.com/css2?family=Open+Sans:wght@400;600;700&display=swap">
<style>
:root{
  --red:#d3141c;
  --red-dark:#8e0f15;
  --red-mid:#b81219;
  --black:#1b1b1b;
  --grey:#6d6e70;
  --silver:#c9c9cb;
  --paper:#ffffff;
  --stage:#ececec;
}
*{box-sizing:border-box;margin:0;padding:0}
html,body{width:1200px;height:1024px;overflow:hidden}
body{background:var(--stage);font-family:"Open Sans",Arial,sans-serif;position:relative;color:var(--grey)}
.sheet{position:absolute;background:var(--paper);overflow:hidden;box-shadow:0 2px 6px rgba(0,0,0,.25)}
.sheet--red{background:radial-gradient(ellipse at 40% 45%,#e3232a 0%,var(--red-mid) 55%,var(--red-dark) 100%)}
.swoosh{position:absolute;left:0;width:100%;display:block}
.swoosh--top{top:0}
.swoosh--bottom{bottom:0;transform:scale(-1,-1)}
.brand{position:absolute;display:flex;align-items:center;gap:8px}
.brand__dot{border-radius:50%;background:var(--red);flex:none}
.brand__name{font-weight:700;color:#58595b;letter-spacing:.02em;line-height:1}
.brand--light .brand__name{color:#fff}
.brand--light .brand__dot{background:#fff}
.fine{font-size:7px;line-height:1.45;color:var(--grey)}
.fine b{color:var(--red);font-weight:600}
.url{position:absolute;font-size:8px;color:#fff}
.deco-circle{position:absolute;border-radius:50%}
/* letterheads */
.letterhead{top:24px;width:345px;height:488px}
.letterhead--front{left:37px}
.letterhead--alt{left:422px}
.letterhead .brand{right:26px;top:66px}
.letterhead .brand__dot{width:22px;height:22px}
.letterhead .brand__name{font-size:15px}
.letterhead__footer{position:absolute;left:0;right:0;bottom:14px;text-align:center}
.letterhead__contacts{position:absolute;left:28px;top:386px}
.cover{left:815px;top:24px;width:344px;height:486px}
.cover .brand{left:0;right:0;top:120px;justify-content:center}
.cover .brand__dot{width:28px;height:28px}
.cover .brand__name{font-size:24px}
/* cards */
.card{top:554px;height:196px}
.card--front{left:36px;width:346px}
.card--back{left:422px;width:346px}
.card--back-alt{left:811px;width:342px}
.card--front .brand{right:26px;top:80px}
.card--front .brand__dot{width:20px;height:20px}
.card--front .brand__name{font-size:16px}
.card__person{position:absolute;left:26px;top:108px}
.card__name{font-size:13px;font-weight:700;color:var(--red);letter-spacing:.02em}
.card__role{font-size:8px;color:var(--grey)}
.card__address{position:absolute;left:26px;top:143px;font-size:8px;line-height:1.4}
.card__phones{position:absolute;left:210px;top:143px;font-size:8px;line-height:1.4}
.card__phones b{color:var(--red)}
.card--back .brand__name,.card--back-alt .brand__name{font-size:17px}
.card__url{font-size:8px;color:#fff;margin-top:2px}
/* envelopes */
.envelope{top:794px;height:180px}
.envelope--front{left:12px;width:380px}
.envelope--back{left:404px;width:385px}
.envelope--red{left:802px;width:389px;height:184px}
.envelope--front .brand{right:26px;top:70px}
.envelope--front .brand__dot{width:20px;height:20px}
.envelope--front .brand__name{font-size:14px}
.envelope__window{position:absolute;left:27px;top:89px;width:148px;height:46px;border-radius:5px;background:linear-gradient(#e4e4e6,#cfcfd2);border:1px solid #bdbdc0}
.envelope__footer{position:absolute;left:0;right:0;bottom:10px;text-align:center}
.flap{position:absolute;inset:0;width:100%;height:100%}
.envelope--red .brand{left:0;right:0;top:14px;flex-direction:column;gap:4px}
.envelope--red .brand__dot{width:16px;height:16px}
.envelope--red .brand__name{font-size:9px}
.dark-url{color:var(--grey)}
</style>
</head>
<body>

<svg width="0" height="0" style="position:absolute">
  <defs>
    <linearGradient id="redBand" x1="0" x2="1" y1="0" y2="0">
      <stop offset="0" stop-color="#8e0f15"/>
      <stop offset=".6" stop-color="#d3141c"/>
      <stop offset="1" stop-color="#e8262d"/>
    </linearGradient>
    <linearGradient id="silverBand" x1="0" x2="1">
      <stop offset="0" stop-color="#9a9a9c"/>
      <stop offset=".5" stop-color="#e6e6e8"/>
      <stop offset="1" stop-color="#bdbdbf"/>
    </linearGradient>
    <symbol id="wave" viewBox="0 0 345 120" preserveAspectRatio="none">
      <path d="M0 0H345V14C250 20 120 40 0 90Z" fill="url(#redBand)"/>
      <path d="M0 90C120 40 250 20 345 14V20C250 28 120 50 0 101Z" fill="#1b1b1b"/>
      <path d="M0 101C120 50 250 28 345 20V25C250 34 120 60 0 110Z" fill="url(#silverBand)"/>
    </symbol>
  </defs>
</svg>

<!-- Letterhead, contacts in footer -->
<section class="sheet letterhead letterhead--front">
  <svg class="swoosh swoosh--top" height="118"><use href="#wave"/></svg>
  <div class="brand"><span class="brand__dot"></span><span class="brand__name">VANTRELLE</span></div>
  <div class="letterhead__footer fine">
    <b>P :</b> +61 3 5550 1827 | <b>M :</b> +61 455 501 936 | <b>E :</b> sales@vantrelle.com.au | <b>ABN :</b> 00 000 000 000<br>
    <b>W :</b> www.vantrelle.com.au | <b>A :</b> Suite xxx, 214 Dawlish Parade Melbourne, Victoria 3000
  </div>
</section>

<!-- Letterhead, wave at both ends -->
<section class="sheet letterhead letterhead--alt">
  <svg class="swoosh swoosh--top" height="118"><use href="#wave"/></svg>
  <div class="brand"><span class="brand__dot"></span><span class="brand__name">VANTRELLE</span></div>
  <div class="letterhead__contacts fine">
    <b>P :</b> +61 3 5550 1827<br>
    <b>M :</b> +61 455 501 936<br>
    <b>E :</b> sales@vantrelle.com.au<br>
    <b>ABN :</b> 00 000 000 000<br>
    Suite xxx, 214 Dawlish Parade Melbourne,<br>Victoria 3000
  </div>
  <svg class="swoosh swoosh--bottom" height="70"><use href="#wave"/></svg>
  <span class="url" style="right:24px;bottom:8px">www.vantrelle.com.au</span>
</section>

<!-- Presentation folder cover -->
<section class="sheet sheet--red cover">
  <div class="brand brand--light"><span class="brand__dot"></span><span class="brand__name">VANTRELLE</span></div>
  <div class="deco-circle" role="img" aria-label="Faint large circle decoration" style="left:110px;top:190px;width:290px;height:290px;background:radial-gradient(circle at 35% 30%,rgba(255,255,255,.22),rgba(255,255,255,.05) 70%)"></div>
  <span class="url" style="left:0;right:0;text-align:center;bottom:20px">www.vantrelle.com.au</span>
</section>

<!-- Business card front -->
<section class="sheet card card--front">
  <svg class="swoosh swoosh--top" height="66"><use href="#wave"/></svg>
  <div class="brand"><span class="brand__dot"></span><span class="brand__name">VANTRELLE</span></div>
  <div class="card__person">
    <div class="card__name">CORBIN HALE</div>
    <div class="card__role">Account Manager</div>
  </div>
  <div class="card__address">Suite xxx, 214 Dawlish Parade<br>Melbourne, Victoria 3000<br><b style="color:var(--red)">W :</b> www.vantrelle.com.au</div>
  <div class="card__phones"><b>P :</b> +61 3 5550 1827<br><b>M :</b> +61 455 501 936<br><b>E :</b> sales@vantrelle.com.au</div>
</section>

<!-- Business card back -->
<section class="sheet sheet--red card card--back">
  <div class="deco-circle" role="img" aria-label="Large silver circle decoration" style="left:12px;top:8px;width:176px;height:176px;background:radial-gradient(circle at 35% 30%,#f4f4f4,#b8b8ba 70%,#8a8a8c)"></div>
  <div class="brand brand--light" style="right:16px;top:138px;flex-direction:column;align-items:flex-end;gap:0">
    <span class="brand__name">VANTRELLE</span>
    <span class="card__url">www.vantrelle.com.au</span>
  </div>
</section>

<!-- Business card back, alternative -->
<section class="sheet sheet--red card card--back-alt">
  <div class="deco-circle" role="img" aria-label="Large silver circle decoration" style="right:22px;top:12px;width:172px;height:172px;background:radial-gradient(circle at 35% 30%,#f4f4f4,#b8b8ba 70%,#8a8a8c)"></div>
  <div class="brand brand--light" style="left:18px;top:146px;flex-direction:column;align-items:flex-start;gap:0">
    <span class="brand__name">VANTRELLE</span>
    <span class="card__url">www.vantrelle.com.au</span>
  </div>
</section>

<!-- DL envelope front -->
<section class="sheet envelope envelope--front">
  <svg class="swoosh swoosh--top" height="62"><use href="#wave"/></svg>
  <div class="brand"><span class="brand__dot"></span><span class="brand__name">VANTRELLE</span></div>
  <div class="envelope__window"></div>
  <div class="envelope__footer fine">
    <b>P :</b> +61 3 5550 1827 | <b>M :</b> +61 455 501 936 | <b>E :</b> sales@vantrelle.com.au | <b>W :</b> www.vantrelle.com.au<br>
    Suite xxx, 214 Dawlish Parade Melbourne, Victoria 3000
  </div>
</section>

<!-- DL envelope back, white -->
<section class="sheet envelope envelope--back">
  <svg class="flap" viewBox="0 0 385 180" preserveAspectRatio="none">
    <path d="M0 2L192 62L385 2" fill="none" stroke="#d8d8da" stroke-width="1.2"/>
  </svg>
  <svg class="swoosh swoosh--top" height="44"><use href="#wave"/></svg>
  <div class="deco-circle" role="img" aria-label="Faint circle decoration" style="left:230px;top:24px;width:130px;height:130px;background:radial-gradient(circle at 35% 30%,rgba(200,200,202,.35),rgba(211,20,28,.12) 75%)"></div>
  <span class="url dark-url" style="left:0;right:0;text-align:center;bottom:10px">www.vantrelle.com.au</span>
</section>

<!-- DL envelope back, red -->
<section class="sheet sheet--red envelope envelope--red">
  <svg class="flap" viewBox="0 0 389 184" preserveAspectRatio="none">
    <path d="M0 2L194 92L389 2" fill="none" stroke="rgba(0,0,0,.25)" stroke-width="1.2"/>
  </svg>
  <div class="brand brand--light"><span class="brand__dot"></span><span class="brand__name">VANTRELLE</span></div>
  <div class="deco-circle" role="img" aria-label="Faint circle decoration" style="right:20px;top:40px;width:130px;height:130px;background:radial-gradient(circle at 35% 30%,rgba(255,255,255,.2),rgba(255,255,255,.04) 70%)"></div>
  <span class="url" style="left:0;right:0;text-align:center;bottom:10px">www.vantrelle.com.au</span>
</section>

</body>
</html>
```